Book on a defense of Christianity needs a cover design.

I need a cover for a book providing a fair and balanced factually supported logical defense of three sources related to Christian beliefs: Elder Codex, Latter Codex, and Scroll of Keravin. It is written in easy to follow language in a father-to-son question and answer format. There are extensive footnotes that allow the reader to go to the source and research all things stated in the book. Both the positive evidence and the negative evidence is presented in respectful language. The final point is a proof of the validity of Christian basic beliefs. The title of the book is: Listen Closely, Child: Where Belief Meets Doubt. Letters from a father to his son regarding an evidence based logical approach to combat the secular attacks on Christianity.
Target Market(s)
General public
Industry/Entity Type
Defense
Requirements
Nice to have
- Color. Attention grabbing design. Can be abstract.

```html
<!DOCTYPE html>
<html lang="en">
<head>
<meta charset="utf-8">
<title>Listen Closely, Child: Where Belief Meets Doubt – Cover Presentation</title>
<link href="https://fonts.googleapis.com/css2?family=Cinzel:wght@400;600;700&family=Crimson+Text:wght@400;600&display=swap" rel="stylesheet">
<style>
  :root {
    --page-bg: #ffffff;
    --parchment-light: #e2c27c;
    --parchment-mid: #c99e4f;
    --parchment-dark: #9c7030;
    --spine-dark: #8a5e24;
    --title-red: #7d1212;
    --title-navy: #0f1a2c;
    --ink: #2a1a08;
    --letter-ink: #f4ecd8;
    --band-blue: #2d4f9e;
    --band-blue-dark: #1f3a80;
    --seal-red: #a8121b;
    --scroll-tone: #e6c684;
    --badge-tone: #f2e8d6;
  }
  html, body {
    margin: 0;
    padding: 0;
    width: 1200px;
    height: 1200px;
    overflow: hidden;
    background: var(--page-bg);
  }
  .sheet { display: block; width: 1200px; height: 1200px; }
  .title-type { font-family: "Cinzel", "Trajan Pro", serif; font-weight: 600; }
  .title-red { fill: var(--title-red); }
  .title-navy { fill: var(--title-navy); }
  .author { font-family: "Cinzel", serif; font-weight: 600; fill: var(--ink); letter-spacing: 0.5px; }
  .letter-text { font-family: "Crimson Text", "Times New Roman", serif; font-size: 7.6px; fill: var(--letter-ink); }
  .blurb { font-family: "Crimson Text", "Times New Roman", serif; font-size: 10.3px; fill: var(--ink); }
  .spine-text { font-family: "Crimson Text", serif; font-size: 13px; letter-spacing: 0.6px; }
</style>
</head>
<body>
<svg class="sheet" viewBox="0 0 1500 1500" xmlns="http://www.w3.org/2000/svg">
  <defs>
    <linearGradient id="parchment" x1="0" y1="0" x2="1" y2="1">
      <stop offset="0" stop-color="var(--parchment-mid)"/>
      <stop offset="0.45" stop-color="var(--parchment-light)"/>
      <stop offset="1" stop-color="var(--parchment-dark)"/>
    </linearGradient>
    <linearGradient id="spine-shade" x1="0" y1="0" x2="1" y2="0">
      <stop offset="0" stop-color="var(--spine-dark)"/>
      <stop offset="0.5" stop-color="var(--parchment-mid)"/>
      <stop offset="1" stop-color="var(--spine-dark)"/>
    </linearGradient>
    <linearGradient id="band" x1="0" y1="0" x2="1" y2="1">
      <stop offset="0" stop-color="var(--band-blue)"/>
      <stop offset="1" stop-color="var(--band-blue-dark)"/>
    </linearGradient>
    <radialGradient id="seal" cx="0.4" cy="0.35" r="0.7">
      <stop offset="0" stop-color="#d22a30"/>
      <stop offset="1" stop-color="var(--seal-red)"/>
    </radialGradient>
    <filter id="drop" x="-5%" y="-5%" width="115%" height="115%">
      <feDropShadow dx="2" dy="3" stdDeviation="2.5" flood-color="#000" flood-opacity="0.35"/>
    </filter>

    <!-- Front cover -->
    <symbol id="front-cover" viewBox="0 0 425 685">
      <rect class="cover-ground" width="425" height="685" fill="url(#parchment)"/>
      <text class="title-type title-red" x="212" y="54" font-size="31" text-anchor="middle" textLength="385" lengthAdjust="spacingAndGlyphs">LISTEN CLOSELY, CHILD:</text>
      <text class="title-type" x="22" y="140" textLength="375" lengthAdjust="spacingAndGlyphs"><tspan class="title-red" font-size="34">WHERE </tspan><tspan class="title-red" font-size="80">BELIEF</tspan></text>
      <text class="title-type title-red" x="212" y="214" font-size="80" text-anchor="middle">MEETS</text>
      <text class="title-type title-navy" x="212" y="270" font-size="56" text-anchor="middle" textLength="378" lengthAdjust="spacing">DOUBT</text>
      <polygon class="torn-band" fill="url(#band)" points="0,288 40,292 90,290 140,298 200,300 250,306 300,304 350,314 390,318 425,326 425,450 380,462 330,478 280,486 230,498 190,514 150,528 110,546 70,560 30,572 0,582"/>
      <g class="letter-text">
        <text x="12" y="330">Dear Dad: The other day in class, one professor said,</text>
        <text x="12" y="340.5">“Religion . . . relies on the gullibility of its clients, who have been</text>
        <text x="12" y="351" textLength="272" lengthAdjust="spacing">educated to believe without evidence and without explanation.” The basic</text>
        <text x="12" y="361.5" textLength="262" lengthAdjust="spacing">assumption is that Christianity has no concrete, scientific “proof”, but is</text>
        <text x="12" y="372" textLength="262" lengthAdjust="spacing">based only on blind and ignorant faith. I have to admit, I’m being shaken</text>
        <text x="12" y="382.5">by this stuff. Is there any physical evidence at all that Jesus lived and</text>
        <text x="12" y="393">that the scriptures are true?</text>
        <text x="12" y="414" textLength="278" lengthAdjust="spacing">Dear Son: Clearly a testimony of spiritual things are spiritual in nature. But</text>
        <text x="12" y="424.5">while you are in this struggle, let me assure you there</text>
        <text x="12" y="435">is compelling physical (empirical) evidence and</text>
        <text x="12" y="445.5">strong logic supporting</text>
        <text x="12" y="456">Christian concepts.</text>
        <text x="12" y="466.5">Let us get started.</text>
      </g>
      <circle class="wax-seal" cx="342" cy="384" r="50" fill="url(#seal)" role="img" aria-label="Red wax seal stamped with a dove"/>
      <rect class="ancient-scroll" x="182" y="462" width="222" height="168" rx="10" fill="var(--scroll-tone)" role="img" aria-label="Unrolled parchment scroll with ancient manuscript lettering"/>
      <text class="author" x="212" y="662" font-size="17" text-anchor="middle">MARTIN L. ARDELL, PHD</text>
    </symbol>

    <!-- Back cover -->
    <symbol id="back-cover" viewBox="0 0 459 685">
      <rect class="cover-ground" width="459" height="685" fill="url(#parchment)"/>
      <text class="title-type title-red" x="215" y="52" font-size="25" text-anchor="middle" textLength="295" lengthAdjust="spacingAndGlyphs">LISTEN CLOSELY, CHILD:</text>
      <circle class="wax-seal" cx="94" cy="119" r="34" fill="url(#seal)" role="img" aria-label="Red wax seal stamped with a dove"/>
      <text class="title-type" x="145" y="109" textLength="208" lengthAdjust="spacingAndGlyphs"><tspan class="title-red" font-size="19">WHERE </tspan><tspan class="title-red" font-size="46">BELIEF</tspan></text>
      <text class="title-type title-red" x="145" y="157" font-size="46" textLength="206" lengthAdjust="spacing">MEETS</text>
      <text class="title-type title-navy" x="138" y="190" font-size="30" textLength="218" lengthAdjust="spacing">DOUBT</text>
      <g class="blurb">
        <text x="22" y="251" textLength="386" lengthAdjust="spacing">Our Christian youth, their parents, and the faithful are being bombarded with secular</text>
        <text x="22" y="265" textLength="386" lengthAdjust="spacing">thinking and ideals. There are loud voices designed to not only discourage active</text>
        <text x="22" y="279" textLength="386" lengthAdjust="spacing">participation in religious practice but to ridicule it. These voices are undercurrents</text>
        <text x="22" y="292">that are receiving increased influence in the world society.</text>
        <text x="22" y="320" textLength="386" lengthAdjust="spacing">We arm our children by teaching them the gospel. We teach them to pray. We teach</text>
        <text x="22" y="334" textLength="386" lengthAdjust="spacing">them to feel the Spirit. We encourage our children to read and ponder the scriptures</text>
        <text x="22" y="347" textLength="386" lengthAdjust="spacing">and to build their own testimonies. We encourage church attendance and other</text>
        <text x="22" y="361" textLength="386" lengthAdjust="spacing">wholesome activities so that they will keep the goals they have set. At the same time,</text>
        <text x="22" y="375" textLength="386" lengthAdjust="spacing">many of the world’s authoritative voices are shouting opposite principles, even ridi-</text>
        <text x="22" y="388">culing and attacking.</text>
        <text x="22" y="416" textLength="386" lengthAdjust="spacing">This book openly acknowledges strengths and weaknesses of both skeptics and de-</text>
        <text x="22" y="430" textLength="386" lengthAdjust="spacing">fenders, weighing each side in consideration of rational, data focused, conclusions</text>
        <text x="22" y="443">that can enable both sides in a civil discussion.</text>
        <text x="22" y="471" textLength="386" lengthAdjust="spacing">Here are specific questions and answers from father to son that will help protect a</text>
        <text x="22" y="485" textLength="386" lengthAdjust="spacing">fragile testimony by arming them with concrete evidence and reason that strongly</text>
        <text x="215" y="498" text-anchor="middle">support a rationally focused religious position.</text>
      </g>
      <text class="author" x="217" y="526" font-size="12.5" text-anchor="middle">MARTIN L. ARDELL, PHD</text>
    </symbol>

    <!-- Spine -->
    <symbol id="spine" viewBox="0 0 33 685">
      <rect width="33" height="685" fill="url(#spine-shade)"/>
      <g transform="translate(16.5 102) rotate(90)" class="spine-text">
        <text x="0" y="-4" fill="var(--title-red)">LISTEN CLOSELY, CHILD:</text>
        <text x="0" y="10" fill="var(--title-red)">WHERE BELIEF MEETS DOUBT</text>
        <text x="250" y="4" fill="var(--ink)">MARTIN L. ARDELL, PHD</text>
      </g>
    </symbol>

    <!-- Full wrap -->
    <symbol id="full-wrap" viewBox="0 0 887 685">
      <use href="#back-cover" x="0" y="0" width="459" height="685"/>
      <use href="#spine" x="459" y="0" width="33" height="685"/>
      <use href="#front-cover" x="462" y="0" width="425" height="685"/>
    </symbol>
  </defs>

  <!-- Row one -->
  <g class="wrap-view" filter="url(#drop)">
    <use href="#full-wrap" x="33" y="28" width="887" height="685"/>
  </g>
  <rect class="preview-badge" x="1080" y="30" width="345" height="42" rx="6" fill="var(--badge-tone)"/>
  <g class="front-view" filter="url(#drop)">
    <use href="#front-cover" x="1015" y="78" width="358" height="577"/>
  </g>

  <!-- Row two -->
  <g class="wrap-view" filter="url(#drop)">
    <use href="#full-wrap" x="33" y="776" width="882" height="681"/>
  </g>
  <rect class="preview-badge" x="1074" y="778" width="345" height="42" rx="6" fill="var(--badge-tone)"/>
  <g class="front-view" filter="url(#drop)">
    <use href="#front-cover" x="1005" y="827" width="362" height="583"/>
  </g>
</svg>
</body>
</html>
```